salami paper bag design The size is 10.5cm 21.5cm 6.7cm

This time we need to make renew salami package design. Planning to make paper salami package. I tried to design but I couldnt formyself.
So please correct my design and recreate more nicer package design from my salami design that attach on the documents.
Logo part I am planning gold stamp. If anybody can make more nicer logo for the package,I don’t mind it.please change the color and shape and everything.
The size is 10.5cm 21.5cm 6.7cm
Thank you.

Target Market(s)

uper market make costomer feel luxurious

Industry/Entity Type

salami matured meat products

Font styles to use
Sans Serif
Decorative
Script

Colors

Designer to choose colors to be used in the design.

Requirements
Nice to have
• Make customer feel joy for genuine fermented salami with wine
Should not have
• My projrct must not have cheap discount design.

```html
<!DOCTYPE html>
<html lang="en">
<head>
<meta charset="utf-8">
<title>Velmont Handmade Salami – Package Front</title>
<link rel="stylesheet" href="https://fonts.googleapis.com/css2?family=Cinzel:wght@400;700&family=Cormorant+Garamond:ital,wght@0,400;0,500;1,500&family=Noto+Sans+JP:wght@400&display=swap">
<style>
  :root {
    --page-bg: #ffffff;
    --silver-light: #f1f1f2;
    --silver-mid: #dadbdd;
    --silver-dark: #c9cacd;
    --gold: #c9961f;
    --gold-soft: #d8a93a;
    --ink: #1c1c1c;
    --band: #161616;
    --white: #ffffff;
    --meat-light: #ece8e0;
    --meat-mid: #d9cfc2;
    --meat-dark: #a87a62;
  }
  * { margin: 0; padding: 0; box-sizing: border-box; }
  html, body {
    width: 1200px; height: 831px; overflow: hidden;
    background: var(--page-bg);
  }
  .stage { position: relative; width: 1200px; height: 831px; }
  .package-front {
    position: absolute; left: 325px; top: 35px;
    width: 549px; height: 760px; overflow: hidden;
    background: linear-gradient(135deg, var(--silver-dark) 0%, var(--silver-mid) 45%, var(--silver-light) 100%);
    box-shadow: 3px 4px 8px rgba(0,0,0,0.25);
    font-family: "Cormorant Garamond", serif;
  }
  .bottom-band {
    position: absolute; left: 0; right: 0; top: 566px; bottom: 0;
    background: var(--band);
  }
  .brand-mark {
    position: absolute; left: 0; right: 0; top: 118px;
    display: flex; justify-content: center; align-items: center; gap: 10px;
  }
  .brand-mark .dot { width: 14px; height: 14px; border-radius: 50%; background: var(--gold); }
  .brand-mark .name {
    font-family: "Cinzel", serif; font-weight: 400; font-size: 24px;
    letter-spacing: 4px; color: var(--gold);
  }
  .quality-arc { position: absolute; left: 174px; top: 236px; width: 200px; height: 40px; }
  .wordmark {
    position: absolute; left: 0; right: 0; top: 268px;
    text-align: center; font-family: "Cinzel", serif; font-weight: 700;
    font-size: 70px; line-height: 84px; color: var(--gold); letter-spacing: 1px;
  }
  .since {
    position: absolute; left: 0; right: 0; top: 360px;
    text-align: center; font-family: "Cormorant Garamond", serif;
    font-size: 21px; color: var(--gold-soft); transform: rotate(-2deg);
  }
  .motto {
    position: absolute; left: 0; right: 0; top: 392px;
    text-align: center; color: var(--ink);
    font-family: "Cormorant Garamond", serif; font-weight: 400;
    font-size: 42px; line-height: 44px; letter-spacing: 0.5px;
  }
  .motto .with {
    font-style: italic; font-weight: 500; font-size: 17px;
    vertical-align: 10px; margin: 0 3px;
  }
  .tagline {
    position: absolute; left: 121px; width: 308px; top: 438px;
    border-top: 1px solid var(--gold); border-bottom: 1px solid var(--gold);
    padding: 3px 0 4px; text-align: center;
    font-family: "Noto Sans JP", sans-serif; font-size: 13px; color: var(--ink);
  }
  .tagline .diamond {
    display: inline-block; width: 4px; height: 4px; background: var(--gold);
    transform: rotate(45deg); vertical-align: middle; margin: 0 12px;
  }
  .product-window {
    position: absolute; left: 93px; top: 475px; width: 367px; height: 180px;
    border: 2px solid var(--gold); border-radius: 8px;
    background: linear-gradient(90deg, var(--meat-light) 0%, var(--meat-mid) 20%, var(--meat-light) 33%,
      var(--meat-mid) 52%, var(--meat-light) 66%, var(--meat-dark) 78%, var(--meat-mid) 90%, var(--meat-light) 100%);
  }
  .product-name {
    position: absolute; left: 0; right: 0; top: 672px;
    text-align: center; font-family: "Cinzel", serif; font-weight: 400;
    font-size: 29px; letter-spacing: 1px; color: var(--white);
  }
  .product-name-jp {
    position: absolute; left: 0; right: 0; top: 710px;
    text-align: center; font-family: "Noto Sans JP", sans-serif;
    font-size: 20px; color: var(--white); letter-spacing: 1px;
  }
</style>
</head>
<body>
<main class="stage">
  <section class="package-front">
    <div class="bottom-band"></div>

    <div class="brand-mark">
      <span class="dot"></span>
      <span class="name">VELMONT</span>
    </div>

    <svg class="quality-arc" viewBox="0 0 200 40">
      <defs><path id="quality-curve" d="M10,38 Q100,-8 190,38"/></defs>
      <text font-family="Cinzel, serif" font-size="14" fill="#d8a93a" letter-spacing="1">
        <textPath href="#quality-curve" startOffset="50%" text-anchor="middle">SUPERIOR QUALITY</textPath>
      </text>
    </svg>

    <div class="wordmark">Velmont</div>
    <div class="since">Since1934</div>

    <div class="motto">CRAFTED<span class="with">With</span>TIME</div>
    <div class="tagline"><span class="diamond"></span>熟成の深い味わいを毎日の食卓へ。<span class="diamond"></span></div>

    <div class="product-window" role="img" aria-label="Window showing whole white-mould cured salami sticks in clear wrap"></div>

    <div class="product-name">HANDMADE SALAMI</div>
    <div class="product-name-jp">自家製生サラミ</div>
  </section>
</main>
</body>
</html>
```